VelloPath Business Card

Our company is called VelloPath and we are based in Tel Aviv, Israel. We create innovative and exciting methods for getting people on the web engaged with content. We need a cool yet professional business card that will represent our management level employees. keep in mind this is a start up company with a young atmosphere. You can be inspired by our logo (file attached, make sure you have the right font "Ubuntu-Condensed") Use the colors that are used in the logo and create a colourful and professional business card.

```html
<!DOCTYPE html>
<html lang="en">
<head>
<meta charset="utf-8">
<title>VelloPath Business Card</title>
<link rel="stylesheet" href="https://fonts.googleapis.com/css2?family=Ubuntu+Condensed&family=Ubuntu:wght@400&display=swap">
<style>
  :root {
    --bg: #d4d4d4;
    --card-white: #ffffff;
    --card-black: #050505;
    --ink: #1a1a1a;
    --brand-blue: #1a8fd6;
    --sky: #5bb8e0;
    --sun: #ffd200;
    --plum: #92278f;
    --magenta: #ec1c79;
  }
  * { box-sizing: border-box; margin: 0; padding: 0; }
  html, body {
    width: 1200px; height: 900px; overflow: hidden;
    background: var(--bg);
  }
  .sheet {
    width: 1200px; height: 900px;
    display: flex; flex-direction: column; align-items: center; justify-content: center;
    gap: 48px;
  }
  .card {
    width: 620px; height: 354px;
    position: relative; overflow: hidden;
    box-shadow: 0 8px 24px rgba(0,0,0,0.18);
  }
  .colour-field {
    background: linear-gradient(to bottom, var(--sky), var(--plum) 40%, var(--magenta) 70%, var(--sun));
  }

  /* Back side */
  .card-back { background: var(--card-black); }
  .card-back .brand {
    position: absolute; left: 40px; bottom: 44px;
    display: flex; align-items: center; gap: 14px;
  }
  .card-back .brand-dot {
    width: 22px; height: 22px; border-radius: 50%; background: var(--brand-blue);
  }
  .card-back .brand-name {
    font-family: "Ubuntu Condensed", "Ubuntu", sans-serif;
    font-size: 46px; color: var(--brand-blue); letter-spacing: 0.5px;
  }

  /* Front side */
  .card-front { background: var(--card-white); display: flex; }
  .edge-band { width: 12px; height: 100%; }
  .info-panel { flex: 1; position: relative; }
  .side-panel { width: 226px; height: 100%; }
  .info-panel .brand {
    position: absolute; left: 0; right: 0; top: 58px;
    display: flex; flex-direction: column; align-items: center; gap: 14px;
  }
  .info-panel .brand-dot {
    width: 40px; height: 40px; border-radius: 50%; background: var(--brand-blue);
  }
  .info-panel .brand-name {
    font-family: "Ubuntu Condensed", "Ubuntu", sans-serif;
    font-size: 42px; color: var(--ink); line-height: 1;
  }
  .contact-list {
    position: absolute; left: 56px; top: 200px;
    list-style: none;
    font-family: "Ubuntu", sans-serif; font-size: 14px; color: var(--ink);
    line-height: 21px; text-align: right; width: 64px;
  }
</style>
</head>
<body>
  <main class="sheet">
    <section class="card card-back" aria-label="Card back">
      <div class="brand">
        <span class="brand-dot"></span>
        <span class="brand-name">VelloPath</span>
      </div>
    </section>

    <section class="card card-front" aria-label="Card front">
      <div class="edge-band colour-field" role="img" aria-label="Multicoloured decorative edge pattern"></div>
      <div class="info-panel">
        <div class="brand">
          <span class="brand-dot"></span>
          <span class="brand-name">VelloPath</span>
        </div>
        <ul class="contact-list">
          <li>Name:</li>
          <li>Web:</li>
          <li>E-mail:</li>
          <li>Tell:</li>
          <li>Address:</li>
        </ul>
      </div>
      <div class="side-panel colour-field" role="img" aria-label="Multicoloured decorative pattern panel"></div>
    </section>
  </main>
</body>
</html>
```